Business card design needed

I am a free lance management consultant looking to have some professionally designed business cards created.
If possible if i could have some bullet points or something with a list of my services that would be great.
Services are:
- Strategic Planning
- Process Improvement
- Change Management
- IT Solutions & Implementation
- IT Consulting
- Web Solutions
Target Market(s)
Business Owners and Operators
Industry/Entity Type
Business
Contact Information for Business Card
Colin Hartley
CH Consulting
0456 318 240
COLIN@COLINHARTLEY.CO
www.colinhartley.co
Logo Text
CH Consulting
Logo styles of interest
Pictorial/Combination Logo
Wordmark Logo
Lettermark Logo

```html
<!DOCTYPE html>
<html lang="en">
<head>
<meta charset="utf-8">
<title>CH Consulting – Business Card</title>
<link rel="stylesheet" href="https://fonts.googleapis.com/css2?family=Roboto+Condensed:wght@700&family=Archivo:wght@700&display=swap">
<style>
  :root {
    --page-bg: #ffffff;
    --card-bg: #ebecec;
    --accent: #e8612a;
    --ink: #111111;
    --muted: #5b5b5b;
    --shadow: #a3a3a3;
    --on-accent: #ffffff;
  }
  html, body {
    margin: 0;
    padding: 0;
    width: 1200px;
    height: 922px;
    overflow: hidden;
    background: var(--page-bg);
  }
  .card {
    position: absolute;
    left: 95px;
    top: 169px;
    width: 1010px;
    height: 583px;
    background: var(--card-bg);
  }
  .card__name,
  .card__company {
    position: absolute;
    top: 140px;
    margin: 0;
    font-family: "Roboto Condensed", "Arial Narrow", sans-serif;
    font-weight: 700;
    font-size: 44px;
    line-height: 1;
    letter-spacing: 0.5px;
  }
  .card__name {
    right: 546px;
    color: var(--accent);
  }
  .card__divider {
    position: absolute;
    left: 475px;
    top: 136px;
    width: 3px;
    height: 87px;
    background: var(--accent);
  }
  .card__company {
    left: 510px;
    color: var(--muted);
    font-size: 41px;
  }
  .contact-shadow {
    position: absolute;
    left: 13px;
    top: 278px;
    width: 473px;
    height: 189px;
    background: var(--shadow);
  }
  .contact {
    position: absolute;
    left: 0;
    top: 266px;
    width: 475px;
    height: 189px;
    background: var(--accent);
    margin: 0;
    padding: 0;
    list-style: none;
  }
  .contact__item {
    position: absolute;
    left: 70px;
    font-family: "Roboto Condensed", "Arial Narrow", sans-serif;
    font-weight: 700;
    font-size: 26px;
    line-height: 1;
    color: var(--on-accent);
    letter-spacing: 0.3px;
  }
  .contact__item--phone { top: 39px; }
  .contact__item--email { top: 85px; }
  .contact__item--web { top: 131px; letter-spacing: 0.8px; }
  .services {
    position: absolute;
    left: 524px;
    top: 230px;
    margin: 0;
    padding: 0;
    list-style: none;
  }
  .services__item {
    position: relative;
    height: 45.3px;
    padding-left: 22px;
    font-family: "Archivo", Arial, sans-serif;
    font-weight: 700;
    font-size: 25px;
    line-height: 1;
    color: var(--ink);
    letter-spacing: 0.9px;
    white-space: nowrap;
  }
  .services__item::before {
    content: "";
    position: absolute;
    left: 0;
    top: 8px;
    width: 9px;
    height: 9px;
    border-radius: 50%;
    background: var(--accent);
  }
</style>
</head>
<body>
  <section class="card" aria-label="Business card for Colin Hartley, CH Consulting">
    <h1 class="card__name">Colin Hartley</h1>
    <div class="card__divider"></div>
    <h2 class="card__company">CH Consulting</h2>

    <div class="contact-shadow"></div>
    <ul class="contact">
      <li class="contact__item contact__item--phone">Mobile: 0456 318 240</li>
      <li class="contact__item contact__item--email">E-mail: colin@colinhartley.co</li>
      <li class="contact__item contact__item--web">www.colinhartley.co</li>
    </ul>

    <ul class="services">
      <li class="services__item">Strategic Planning</li>
      <li class="services__item">Process Improvement</li>
      <li class="services__item">Change Management</li>
      <li class="services__item">IT Solutions &amp; Implementation</li>
      <li class="services__item">IT Consulting</li>
      <li class="services__item">Web Solutions</li>
    </ul>
  </section>
</body>
</html>
```